Australian Meat, Seafood and Fresh Produce Website

Our organization is looking to design a simple, but eye catching website to show our services.
Our company exports West Australian FRESH fruit and vegetables, seafood and meat.
The website we are looking for would consist of:
- Landing Page
- Company info
- Directors bio
- Page that highlights our products
- Contact us page
We would like it to have a Chinese translated version as well.
Tobin
Target Market(s)
Chinese Market
Industry/Entity Type
It Company
Number of Pages Required
1 page
Look and feel
Each slider illustrates characteristics of the customer's brand and the style your logo design should communicate.

```html
<!DOCTYPE html>
<html lang="en">
<head>
<meta charset="utf-8">
<title>Swanvale Foods Direct</title>
<link href="https://fonts.googleapis.com/css2?family=Open+Sans:wght@400;600;700&family=Yanone+Kaffeesatz:wght@300;400&family=Oswald:wght@400&display=swap" rel="stylesheet">
<style>
:root{
  --orange:#f26b1d;
  --blue:#8fc3d6;
  --band:#97c8d8;
  --text:#333;
  --muted:#555;
  --line:#dcdcdc;
  --foot:#e1e1e1;
  --bar:#3b3b3b;
  --white:#fff;
}
*{box-sizing:border-box;margin:0;padding:0}
html,body{width:763px;height:1200px;overflow:hidden}
body{position:relative;background:var(--white);font-family:"Open Sans",sans-serif;color:var(--text)}
.abs{position:absolute}
.brand{left:48px;top:14px;font:600 22px/1 "Open Sans",sans-serif;color:var(--orange);display:flex;align-items:center;gap:8px}
.brand .mark{width:18px;height:18px;background:var(--orange)}
.utility{right:46px;top:12px;font-size:8.5px;color:#444;letter-spacing:.3px}
.nav{right:46px;top:42px;display:flex;gap:32px;font:600 10px/1 "Open Sans",sans-serif;color:#333}
.nav .active{color:var(--orange)}
.hero{left:0;top:62px;width:763px;height:303px;background:linear-gradient(100deg,#e8c13a 0%,#7cab3d 22%,#c8392a 38%,#8fb34a 55%,#b8323a 72%,#8a5a34 100%)}
.arrow{top:200px;width:29px;height:29px;border-radius:50%;background:var(--white);border:2px solid #222;display:flex;align-items:center;justify-content:center}
.hero-caption{left:38px;top:296px;width:324px;height:38px;background:var(--orange);color:var(--white);font:400 28px/38px "Yanone Kaffeesatz",sans-serif;padding-left:10px;letter-spacing:.3px}
.welcome{left:47px;top:390px;width:669px;display:flex;align-items:center;gap:8px}
.welcome .rule{height:1.5px;background:var(--line)}
.welcome h1{font:300 27px/1 "Yanone Kaffeesatz",sans-serif;color:var(--blue);white-space:nowrap}
.intro{left:47px;top:428px;width:670px;font-size:8.6px;line-height:14px;color:#444}
.intro p+p{margin-top:14px}
.divider{left:47px;width:669px;height:1px;background:var(--line)}
.section-title{font:300 22px/1 "Yanone Kaffeesatz",sans-serif;color:var(--blue)}
.member{display:flex;gap:8px;width:165px}
.portrait{width:57px;height:72px;flex:none;background:linear-gradient(160deg,#d9d9d9,#8e8a86)}
.member h3{font:700 10.5px/1.2 "Open Sans",sans-serif;color:#222;letter-spacing:.3px;margin-top:-1px}
.member p{font-size:8.6px;line-height:11.5px;margin-top:6px;color:#333}
.supplier{width:110px}
.supplier .logo{height:44px;display:flex;align-items:center;gap:5px;font:600 11px/1 "Open Sans",sans-serif;color:#777}
.supplier .logo i{width:12px;height:12px;border-radius:50%;background:#9a9a9a;flex:none}
.supplier h3{margin-top:24px;font:700 10.5px/14px "Open Sans",sans-serif;color:#222;height:28px}
.supplier p{margin-top:6px;font-size:8.6px;line-height:12px;height:36px}
.supplier .more{font:700 8px/1 "Open Sans",sans-serif;color:var(--blue)}
.product{top:800px;width:211px;height:165px}
.product .photo{height:137px}
.product .label{height:28px;background:var(--band);color:var(--white);font:400 15px/28px "Yanone Kaffeesatz",sans-serif;padding-left:12px;letter-spacing:.3px}
.footer{left:0;top:1000px;width:763px;height:167px;background:var(--foot)}
.fcol{top:1020px;width:155px}
.fcol h4{font:400 12px/1 "Oswald",sans-serif;color:#333;text-transform:uppercase;transform:scaleX(.85);transform-origin:left;padding-bottom:8px;border-bottom:1px solid #c8c8c8;width:182px}
.fcol ul{list-style:none;margin-top:10px;font-size:8.6px;line-height:13.5px}
.news{margin-top:10px}
.news small{font-size:6.5px;display:block;color:#444}
.news p{font-size:8.6px;line-height:13px;margin-bottom:10px}
.contact{display:flex;align-items:center;gap:8px;font-size:8.6px;line-height:12px;margin-top:8px}
.contact svg{flex:none}
.email-field{margin-top:8px;width:154px;height:20px;background:var(--white);border:1px solid #d0d0d0;font-size:7.5px;color:#888;padding:5px 5px}
.subscribe{margin-top:8px;width:70px;height:20px;background:var(--orange);color:var(--white);font:700 9px/20px "Open Sans",sans-serif;text-align:center}
.bottom{left:0;top:1167px;width:763px;height:33px;background:var(--bar);color:var(--white);font-size:8.5px;line-height:33px;padding-left:48px}
.socials{right:47px;top:1173px;display:flex;gap:5px}
.socials span{width:21px;height:21px;border-radius:50%;border:1.5px solid var(--white)}
</style>
</head>
<body>
<header>
  <div class="abs brand"><span class="mark"></span>Swanvale Foods Direct</div>
  <div class="abs utility">HELP | JOIN | LOG IN</div>
  <nav class="abs nav"><span class="active">HOME</span><span>ABOUT US</span><span>SERVICES</span><span>PRODUCTS</span><span>CONTACT US</span></nav>
</header>

<section class="abs hero" role="img" aria-label="Fresh produce display: corn, peppers, asparagus, grapes, apples and leafy greens in a wooden crate"></section>
<div class="abs arrow" style="left:40px"><svg width="12" height="12" viewBox="0 0 12 12"><path d="M8 1 3 6l5 5" fill="none" stroke="#222" stroke-width="2"/></svg></div>
<div class="abs arrow" style="left:693px"><svg width="12" height="12" viewBox="0 0 12 12"><path d="M4 1l5 5-5 5" fill="none" stroke="#222" stroke-width="2"/></svg></div>
<div class="abs hero-caption">LOREM IPSUM DOLOR SIT AMET</div>

<section>
  <div class="abs welcome"><span class="rule" style="width:23px"></span><h1>Welcome to Swanvale Foods Direct</h1><span class="rule" style="flex:1"></span></div>
  <div class="abs intro">
    <p>Swanvale Foods Direct (SVFD) aims to supply high quality West Australian produce to the rest of the World. Western Australia is known for its high quality farming practices and environment, which produces meat, seafood, fruit and vegetable of a caliber that is respected globally.</p>
    <p>With a management team and first class suppliers allows our organization to provide quality ingredients, straight from farm or ocean to purchaser, in a timely manner to the highest quality.</p>
  </div>
</section>
<div class="abs divider" style="top:511px"></div>

<section>
  <h2 class="abs section-title" style="left:47px;top:528px">The Management Team</h2>
  <div class="abs member" style="left:47px;top:569px"><div class="portrait" role="img" aria-label="Portrait of Jared Tobin"></div><div><h3>JARED TOBIN</h3><p>Management of operations, Chinese liaison, Quality processes and management.</p></div></div>
  <div class="abs member" style="left:219px;top:569px"><div class="portrait" role="img" aria-label="Portrait of Marcus Hale"></div><div><h3>MARCUS HALE</h3><p>Procurement and liaison with suppliers.</p></div></div>
  <div class="abs member" style="left:47px;top:659px"><div class="portrait" role="img" aria-label="Portrait of Owen Pritchard"></div><div><h3>OWEN PRITCHARD</h3><p>Logistics, transport, customs and tariffs</p></div></div>
  <div class="abs member" style="left:219px;top:659px"><div class="portrait" role="img" aria-label="Portrait of Dr Mei Zhou"></div><div><h3>DR MEI ZHOU</h3><p>Chinese Market Specialist, liaison between Australia and Chinese activities.</p></div></div>
</section>

<section>
  <h2 class="abs section-title" style="left:390px;top:528px">The Suppliers</h2>
  <div class="abs supplier" style="left:390px;top:568px"><div class="logo"><i></i>Prime Field</div><h3>PRIME FIELD DISTRIBUTORS</h3><p>High quality beef, lamb and pork</p><div class="more">MORE ›</div></div>
  <div class="abs supplier" style="left:504px;top:568px"><div class="logo"><i></i>Orchardine</div><h3>ORCHARDINE</h3><p>Fresh Fruit and Vegetables</p><div class="more">MORE ›</div></div>
  <div class="abs supplier" style="left:619px;top:568px"><div class="logo"><i></i>Harbourline</div><h3>HARBOURLINE</h3><p>Fresh Seafood</p><div class="more">MORE ›</div></div>
</section>
<div class="abs divider" style="top:749px"></div>

<section>
  <h2 class="abs section-title" style="left:47px;top:765px">Our Products</h2>
  <div class="abs product" style="left:47px"><div class="photo" role="img" aria-label="Wooden crates of fresh fruit and vegetables" style="background:linear-gradient(135deg,#b88a5a,#7fa24a 45%,#c24a3a 75%,#9a7a4a)"></div><div class="label">FRESH FRUIT &amp; VEGETABLES</div></div>
  <div class="abs product" style="left:276px"><div class="photo" role="img" aria-label="Lobster, fish fillets and prawns on ice" style="background:linear-gradient(120deg,#7a4a34,#d8a08a 45%,#f08a5a 70%,#e0c8b8)"></div><div class="label">FRESH SEAFOOD</div></div>
  <div class="abs product" style="left:505px"><div class="photo" role="img" aria-label="Raw cut of red meat on white" style="background:radial-gradient(ellipse at 55% 55%,#b8323a 0%,#d8848a 40%,#f4f4f4 70%)"></div><div class="label">FRESH MEAT</div></div>
</section>

<footer>
  <div class="abs footer"></div>
  <div class="abs fcol" style="left:47px"><h4>Navigation</h4><ul><li>Home</li><li>About Us</li><li>Services</li><li>Products</li><li>Contact Us</li></ul></div>
  <div class="abs fcol" style="left:219px"><h4>Recent News</h4>
    <div class="news"><small>January 28, 2013 - 11:49am</small><p>Lorem ipsum dolor sit amet, consec tetur adipiscing elit</p><small>January 28, 2013 - 11:49am</small><p>Lorem ipsum dolor sit amet, consec tetur adipiscing elit</p></div></div>
  <div class="abs fcol" style="left:390px"><h4>Contact Info</h4>
    <div class="contact"><svg width="18" height="18" viewBox="0 0 18 18"><circle cx="9" cy="9" r="8" fill="none" stroke="#555"/><path d="M9 4a3 3 0 0 0-3 3c0 2.5 3 6 3 6s3-3.5 3-6a3 3 0 0 0-3-3z" fill="#555"/></svg><span>258, Lorem Ipsum dolor amet<br>Dosis amet sit - 558895</span></div>
    <div class="contact"><svg width="18" height="18" viewBox="0 0 18 18"><circle cx="9" cy="9" r="8" fill="none" stroke="#555"/><path d="M6 5l2 0 1 2-1 1a5 5 0 0 0 2 2l1-1 2 1v2c-4 0-7-3-7-7z" fill="#555"/></svg><span>Phone: 1-555-010-2030</span></div>
    <div class="contact"><svg width="18" height="18" viewBox="0 0 18 18"><circle cx="9" cy="9" r="8" fill="none" stroke="#555"/><path d="M5 7l4-2 4 2v5H5z" fill="none" stroke="#555"/><path d="M5 7l4 3 4-3" fill="none" stroke="#555"/></svg><span>Email: info@swanvalefoods.com</span></div>
  </div>
  <div class="abs fcol" style="left:562px"><h4 style="width:154px">Subscribe our Newsletter</h4>
    <p style="font-size:8.6px;line-height:13px;margin-top:10px">Lorem ipsum dolor sit amet, consectetur adipiscing elit.</p>
    <div class="email-field">Enter Your Email</div>
    <div class="subscribe">SUBSCRIBE</div></div>
  <div class="abs bottom">© 2015 Swanvale Foods Direct. All Rights Reserved.</div>
  <div class="abs socials"><span></span><span></span><span></span><span></span></div>
</footer>
</body>
</html>
```